Sproutwell

I need a product label that will be adhered to a square cardboard box. The label should be 8 inches by 8 inches. Contained within the box is a pot derived from 100% sustainable CocoCoir, a soil mix comprised of CocoCoir and Humus Compost, along with the plant drip tray. The brand name for the product is Fern4Home. I have attached a rough markup for an example

```html
<!DOCTYPE html>
<html lang="en">
<head>
<meta charset="utf-8">
<title>Sproutwell Container Garden Kit Label</title>
<link href="https://fonts.googleapis.com/css2?family=Josefin+Sans:wght@400;600&family=Quicksand:wght@500;600&display=swap" rel="stylesheet">
<style>
  :root {
    --bg: #e1ebe2;
    --paper: #f2ebdc;
    --paper-edge: #e9dfca;
    --green: #3cb450;
    --green-soft: #55c065;
    --plant-tone: #d9d3c2;
    --pot-top: #b98a55;
    --pot-bottom: #9c6c3c;
  }
  * { margin: 0; padding: 0; box-sizing: border-box; }
  html, body { width: 1200px; height: 1056px; overflow: hidden; background: var(--bg); }
  .label {
    position: absolute; left: 130px; top: 58px; width: 940px; height: 940px;
    background: radial-gradient(circle at 40% 30%, #f6f0e3 0%, var(--paper) 60%, var(--paper-edge) 100%);
    border-radius: 34px;
    font-family: "Josefin Sans", sans-serif;
    color: var(--green);
  }
  .kit-type {
    position: absolute; top: 72px; left: 0; width: 100%; text-align: center;
    font-size: 30px; font-weight: 400; letter-spacing: 0.5px;
  }
  .brand {
    position: absolute; top: 140px; left: 0; width: 100%;
    display: flex; justify-content: center; align-items: center; gap: 18px;
  }
  .brand-dot { width: 34px; height: 34px; border-radius: 50%; background: var(--green); }
  .brand-name { font-size: 66px; font-weight: 600; letter-spacing: 2px; line-height: 1; padding-top: 8px; }
  .eco-badge {
    position: absolute; top: 38px; right: 40px; width: 118px; height: 118px;
    border-radius: 50%; border: 5px solid var(--green);
  }
  .illustration {
    position: absolute; left: 290px; top: 320px; width: 340px; height: 610px;
    background: linear-gradient(to bottom, var(--plant-tone) 0%, var(--plant-tone) 58%, var(--pot-top) 62%, var(--pot-bottom) 100%);
    border-radius: 20px 20px 12px 12px;
    opacity: 0.9;
  }
  .checklist { position: absolute; left: 560px; top: 500px; width: 340px; height: 430px; }
  .checklist svg { position: absolute; inset: 0; }
  .checklist-body { position: absolute; left: 78px; top: 70px; right: 20px; font-family: "Quicksand", sans-serif; }
  .checklist-title { font-family: "Josefin Sans", sans-serif; font-size: 30px; font-weight: 400; margin-bottom: 22px; }
  .checklist-items { list-style: none; }
  .checklist-items li { font-size: 14.5px; font-weight: 500; margin-bottom: 22px; white-space: nowrap; }
  .checklist-items .qty { font-weight: 600; margin-right: 6px; }
  .checklist-note { font-size: 14.5px; font-weight: 500; margin-top: 34px; }
  .recycle-mark {
    position: absolute; left: 78px; top: 868px; width: 66px; height: 66px;
    border-radius: 50%; background: var(--green);
  }
</style>
</head>
<body>
  <main class="label">
    <p class="kit-type">Container Garden Kit</p>
    <div class="brand">
      <span class="brand-dot"></span>
      <span class="brand-name">Sproutwell</span>
    </div>
    <div class="eco-badge" aria-hidden="true"></div>

    <div class="illustration" role="img" aria-label="Line drawing of a fruiting tomato plant growing in a coco coir pot"></div>

    <section class="checklist">
      <svg width="340" height="430" viewBox="0 0 340 430" aria-hidden="true">
        <path d="M30 18 L318 2 L322 400 L36 428 Z" fill="none" stroke="#3cb450" stroke-width="2"/>
        <g fill="none" stroke="#3cb450" stroke-width="2">
          <circle cx="40" cy="45" r="9"/><circle cx="40" cy="80" r="9"/><circle cx="40" cy="115" r="9"/>
          <circle cx="40" cy="150" r="9"/><circle cx="40" cy="185" r="9"/><circle cx="40" cy="220" r="9"/>
          <circle cx="40" cy="255" r="9"/><circle cx="40" cy="290" r="9"/><circle cx="40" cy="325" r="9"/>
          <circle cx="40" cy="360" r="9"/><circle cx="40" cy="395" r="9"/>
        </g>
      </svg>
      <div class="checklist-body">
        <h2 class="checklist-title">This kit includes:</h2>
        <ul class="checklist-items">
          <li><span class="qty">1</span>12" Eco-friendly CocoCoir pot</li>
          <li><span class="qty">1</span>Cubic foot of potting soil mix</li>
          <li><span class="qty">4</span>Packets of balanced plant food</li>
          <li><span class="qty">1</span>8oz bottle of Vireo</li>
          <li><span class="qty">1</span>Drip Tray</li>
        </ul>
        <p class="checklist-note">With easy to grow instructions!</p>
      </div>
    </section>

    <div class="recycle-mark" aria-hidden="true"></div>
  </main>
</body>
</html>
```